Lumen Drift The Velvet Nook needs a room spray label

We are a company that is dedicated to the aromatization services for our customers, we have just created an aromatic product that is a Room Spray for the customer to spray it in their spaces and we are looking for the most sophisticated and luxurious label in the market, help us? Thanks a lot!

Target Market(s)

That the label represents an elegant and exclusive aroma

Font styles to use
Serif

Colors

Designer to choose colors to be used in the design.

Requirements
Must have
• Elegance, fine, luxury and cleanliness
Nice to have
• The fonts I like are those of the logo, they are called "Cinzel_Regular" and "MrEaveXL"
They can propose in color but I think it looks better in black and gray or white, however I would like to see something in color

```html
<!DOCTYPE html>
<html lang="es">
<head>
<meta charset="utf-8">
<title>Lumen Drift – Room Spray Label</title>
<link href="https://fonts.googleapis.com/css2?family=Cinzel:wght@400;700&display=swap" rel="stylesheet">
<style>
  :root {
    --page-bg: #e6e6e6;
    --label-white: #fbfbfb;
    --gold-deep: #c9922f;
    --gold-mid: #d9ad4a;
    --gold-light: #e3cb66;
    --gold-text: #c99a2e;
    --ink: #1d1d1d;
  }
  html, body {
    margin: 0;
    padding: 0;
    width: 950px;
    height: 1200px;
    overflow: hidden;
    background: var(--page-bg);
  }
  .label {
    position: absolute;
    left: 285px;
    top: 30px;
    width: 380px;
    height: 1140px;
    background: var(--label-white);
    font-family: 'Cinzel', serif;
    text-align: center;
  }
  .band {
    position: absolute;
    left: 0;
    width: 100%;
    background: linear-gradient(90deg, var(--gold-deep), var(--gold-mid) 55%, var(--gold-light));
  }
  .band--top { top: 51px; height: 47px; }
  .band--bottom {
    top: 1029px;
    height: 77px;
    display: flex;
    align-items: center;
    justify-content: center;
    font-size: 30px;
    color: var(--ink);
    letter-spacing: 1px;
  }
  .rule {
    position: absolute;
    height: 2px;
    background: var(--gold-deep);
  }
  .rule--footer { left: 0; width: 100%; top: 1011px; height: 4px; background: var(--gold-mid); }
  .rule--upper { left: 35px; width: 310px; top: 568px; }
  .rule--lower { left: 70px; width: 240px; top: 650px; }
  .brand-mark {
    position: absolute;
    left: 120px;
    top: 150px;
    width: 140px;
    height: 140px;
    border: 3px solid var(--gold-text);
    border-radius: 50%;
    box-sizing: border-box;
  }
  .brand-name {
    position: absolute;
    left: 0;
    width: 100%;
    top: 400px;
    margin: 0;
    color: var(--gold-text);
    font-weight: 400;
    font-size: 40px;
    line-height: 1;
  }
  .brand-tagline {
    display: block;
    margin-top: 8px;
    font-size: 15px;
    letter-spacing: 7px;
  }
  .ornament {
    position: absolute;
    background: radial-gradient(ellipse at center, var(--gold-mid), rgba(217,173,74,0.25) 70%, transparent);
  }
  .ornament--upper { left: 140px; top: 516px; width: 100px; height: 52px; border-radius: 50% 50% 0 0; }
  .ornament--lower { left: 160px; top: 652px; width: 60px; height: 40px; border-radius: 0 0 50% 50%; }
  .product-name {
    position: absolute;
    left: 0;
    width: 100%;
    top: 585px;
    margin: 0;
    font-weight: 400;
    font-size: 44px;
    letter-spacing: 4px;
    color: var(--ink);
    line-height: 1;
  }
  .claim {
    position: absolute;
    left: 0;
    width: 100%;
    top: 748px;
    margin: 0;
    color: var(--ink);
    line-height: 1;
  }
  .claim__percent {
    display: block;
    font-weight: 700;
    font-size: 38px;
    color: var(--gold-text);
  }
  .claim__blend { display: block; font-size: 20px; margin-top: 14px; }
  .claim__type { display: block; font-size: 31px; margin-top: 10px; }
  .claim__net { display: block; font-size: 20px; margin-top: 10px; }
</style>
</head>
<body>
  <div class="label">
    <div class="band band--top"></div>

    <div class="brand-mark" aria-hidden="true"></div>
    <h1 class="brand-name">Lumen Drift<span class="brand-tagline">The Velvet Nook</span></h1>

    <div class="ornament ornament--upper" role="img" aria-label="Golden leaf ornament"></div>
    <div class="rule rule--upper"></div>
    <h2 class="product-name">DAPPER</h2>
    <div class="rule rule--lower"></div>
    <div class="ornament ornament--lower" role="img" aria-label="Small golden leaf ornament"></div>

    <p class="claim">
      <span class="claim__percent">100%</span>
      <span class="claim__blend">MEZCLA DE ACEITES</span>
      <span class="claim__type">AROMATICOS</span>
      <span class="claim__net">CONTENIDO NETO</span>
    </p>

    <div class="rule rule--footer"></div>
    <div class="band band--bottom">60ML</div>
  </div>
</body>
</html>
```